Awesome photographers card for an awesome new business

Double sided business card Black background and silver logo in middle on one side. Details on otherside. please keep it simple

Industry/Entity Type

Photographer

Contact Information for Business Card

Colin Fairweather
0452816307
ColinFairweatherPhotography57@mailvane.com
www.ColinFairweatherPhotography.com.au
Instagram _Colin_fairweather

Requirements
Must have
• My logo in Silver
• please use instagram logo instead of "Instagram"

```html
<!DOCTYPE html>
<html lang="en">
<head>
<meta charset="utf-8">
<title>Colin Fairweather Photography – Business Card</title>
<link rel="stylesheet" href="https://fonts.googleapis.com/css2?family=Open+Sans:wght@400;600&display=swap">
<style>
  :root {
    --backdrop: #2e2725;
    --card-light: #f7f7f5;
    --card-dark: #0d0d0d;
    --ink: #1c1c1c;
    --ink-soft: #3a3a3a;
    --silver: #b9b9b9;
    --silver-dark: #9a9a9a;
  }
  * { margin: 0; padding: 0; box-sizing: border-box; }
  html, body { width: 1200px; height: 844px; overflow: hidden; }
  body {
    background: var(--backdrop);
    font-family: "Open Sans", sans-serif;
    position: relative;
  }
  .card {
    position: absolute;
    top: 272px;
    width: 520px;
    height: 300px;
  }
  .card--front { left: 50px; background: var(--card-light); }
  .card--back { left: 630px; background: var(--card-dark); }

  .brand {
    display: flex;
    align-items: center;
    gap: 10px;
    position: absolute;
    font-weight: 600;
    letter-spacing: 0.12em;
    text-transform: uppercase;
  }
  .brand__dot {
    width: 14px; height: 14px;
    border-radius: 50%;
    background: currentColor;
    flex: none;
  }
  .card--front .brand {
    top: 40px; right: 36px;
    color: var(--silver-dark);
    font-size: 13px;
  }
  .card--back .brand {
    top: 50%; left: 50%;
    transform: translate(-50%, -50%);
    color: var(--silver);
    font-size: 17px;
    white-space: nowrap;
  }

  .details {
    position: absolute;
    left: 40px;
    bottom: 34px;
    color: var(--ink-soft);
  }
  .details__name {
    font-size: 19px;
    font-weight: 600;
    color: var(--ink);
    letter-spacing: 0.02em;
    text-transform: uppercase;
    margin-bottom: 10px;
  }
  .details__handle {
    display: flex; align-items: center; gap: 7px;
    font-size: 15px;
    margin-bottom: 22px;
  }
  .details__social {
    width: 14px; height: 14px;
    background: var(--ink-soft);
    border-radius: 3px;
  }
  .contact-list { list-style: none; }
  .contact-list li {
    display: flex; align-items: center; gap: 6px;
    font-size: 13.5px;
    line-height: 18px;
    color: var(--ink);
  }
  .contact-list svg { width: 11px; height: 11px; flex: none; fill: var(--ink-soft); }
</style>
</head>
<body>
  <section class="card card--front">
    <div class="brand"><span class="brand__dot"></span>Colin Fairweather</div>
    <div class="details">
      <h1 class="details__name">Colin Fairweather</h1>
      <p class="details__handle"><span class="details__social"></span>Colin_fairweather</p>
      <ul class="contact-list">
        <li>
          <svg viewBox="0 0 12 12"><path d="M2.5 0.8 4.2 3 3.3 4.3c.7 1.6 2.1 3 3.9 3.9L8.5 7.3l2.2 1.7-1 2.1C5 10.6 1.3 7 0.8 2.2z"/></svg>
          0452816307
        </li>
        <li>
          <svg viewBox="0 0 12 12"><circle cx="6" cy="6" r="5.5"/><path d="M1 6h10M6 .5c-2.2 3-2.2 8 0 11M6 .5c2.2 3 2.2 8 0 11" stroke="#f7f7f5" stroke-width="0.9" fill="none"/></svg>
          www.ColinFairweatherPhotography.com.au
        </li>
        <li>
          <svg viewBox="0 0 12 12"><rect x="0.5" y="2" width="11" height="8" rx="1"/><path d="M1 2.6 6 6.6l5-4" stroke="#f7f7f5" stroke-width="1" fill="none"/></svg>
          ColinFairweatherPhotography57@mailvane.com
        </li>
      </ul>
    </div>
  </section>

  <section class="card card--back">
    <div class="brand"><span class="brand__dot"></span>Colin Fairweather</div>
  </section>
</body>
</html>
```